Contemporary Literature/Novel Needs Book Cover Design

This fiction novel is entitled "Before the Tide Turns".
This is a literary fiction piece of work, with the protagonist a female mathematician. The general precis of the novel is her life and her overriding sentimentality that everything on Earth - all life, all memories, all love, all of the events we ever experienced, will all vanish without a trace when the sun dies. I am looking for a classic looking book cover in keeping with the literary feel of the novel, but also something that ties in the mathematics / astronomy of the protagonist's work, and of course the actual title of the book.
The protagonist is a female, the book covers the period of her life from 20 years of age to the late 40's. By "Classic" look I mean: expensive and timeless; something that could have been written 100 years ago, or today.
Please contact me for any further clarifications.
Updates

Reason: Extending deadline to allow for the Easter holiday period as I will b e offline for the next 2 days.

Target Market(s)

Contemporary literature buyers

Industry/Entity Type

Work

Font styles to use
Script

Requirements
Must have
• Cover design that reflects the brief / precis of the novel.
• Author: R.K Fenwick
Should not have
• Images of people

```html
<!DOCTYPE html>
<html lang="en">
<head>
<meta charset="utf-8">
<title>Before the Tide Turns — R.K Fenwick</title>
<link href="https://fonts.googleapis.com/css2?family=Great+Vibes&family=Bodoni+Moda:wght@400&display=swap" rel="stylesheet">
<style>
  :root {
    --ink: #121212;
    --page: #ffffff;
    --core-glow: #fde3c4;
    --core-warm: #f0a77e;
    --arm-rose: #c98a78;
    --dust-violet: #6f6a86;
    --space-blue: #2f3a5e;
    --deep-space: #141a33;
  }
  * { margin: 0; padding: 0; box-sizing: border-box; }
  html, body {
    width: 804px;
    height: 1200px;
    overflow: hidden;
    background: var(--page);
  }
  .cover {
    position: relative;
    width: 804px;
    height: 1200px;
    overflow: hidden;
    background: var(--page);
  }
  .cover__sky {
    position: absolute;
    left: 9px;
    top: 12px;
    width: 786px;
    height: 1180px;
    background:
      radial-gradient(ellipse 55% 40% at 10% 60%, var(--core-glow) 0%, var(--core-warm) 30%, var(--arm-rose) 55%, transparent 80%),
      radial-gradient(ellipse 80% 60% at 20% 55%, var(--dust-violet) 0%, transparent 75%),
      linear-gradient(160deg, var(--deep-space) 0%, var(--space-blue) 45%, var(--dust-violet) 75%, var(--space-blue) 100%);
  }
  .cover__orbits {
    position: absolute;
    inset: 0;
    width: 804px;
    height: 1200px;
  }
  .cover__orbits .stroke {
    fill: none;
    stroke: var(--ink);
    stroke-width: 9;
  }
  .cover__orbits .sun {
    fill: var(--ink);
  }
  .cover__title {
    position: absolute;
    right: 56px;
    top: 620px;
    font-family: "Great Vibes", cursive;
    font-weight: 400;
    font-size: 82px;
    line-height: 1;
    color: var(--ink);
    white-space: nowrap;
  }
  .cover__author {
    position: absolute;
    right: 56px;
    top: 768px;
    font-family: "Bodoni Moda", serif;
    font-weight: 400;
    font-size: 56px;
    line-height: 1;
    color: var(--ink);
    white-space: nowrap;
  }
</style>
</head>
<body>
  <main class="cover">
    <div class="cover__sky" role="img" aria-label="Photograph of a spiral galaxy with a glowing peach core and blue starry arms"></div>

    <svg class="cover__orbits" viewBox="0 0 804 1200" aria-hidden="true">
      <defs>
        <clipPath id="lower-field">
          <rect x="9" y="733" width="786" height="459"/>
        </clipPath>
      </defs>
      <rect class="stroke" x="9" y="12" width="786" height="1180"/>
      <line class="stroke" x1="9" y1="733" x2="795" y2="733"/>
      <g clip-path="url(#lower-field)">
        <circle class="stroke" cx="90" cy="733" r="110"/>
        <circle class="stroke" cx="90" cy="733" r="210"/>
        <circle class="stroke" cx="90" cy="733" r="320"/>
      </g>
      <circle class="sun" cx="90" cy="733" r="22"/>
    </svg>

    <h1 class="cover__title">Before the Tide Turns</h1>
    <p class="cover__author">R.K Fenwick</p>
  </main>
</body>
</html>
```